Computer business needs new look.

KELD Computers has been selling and repairing, servicing computers in northern NSW for 20 years and has now branched out into Surveillance/ CCTV systems Alarm systems and just about anything technical.
We have also changed our area of operation from just the northern rivers to include all of outback New South Wales and Queensland.
We have changed our name slightly to K.E.L.D Sundown Technical Services.I will include my old business card.The Logo can stay or go i am open to all designs.
Updates

facebook page for info https://www.examplebook.test/pages/KELD-Computers/482019375610283?fref=ts The top half of the business card i uploaded looks pink ! it should be white

I should have mentioned this before. My new look cards will become the look of the business. ie: advertising, vehicle sign-writing etc: The look that i think im after is more to large business/corporate look not "WALLY THE FIXER " Probably the main focus is the fact that we service the small towns in outback Australia. " Billabong Barney " Not just the big city's Please feel free to through any thing at me and any questions please ask.

I have uploaded a picture that i would like the back of the card to look like. Please have a look and see what you can do.

Reason: I am hoping to get some original designs that i like. So far i have just 1 that i like..there must be more ideas out there.

Target Market(s)

Small to medium business

Industry/Entity Type

Business

Contact Information for Business Card

K.E.L.D Sundown Technical Services
Owen Pelkie
1300621745 0457 318206

Requirements
Nice to have
• Back of card to have a list of services
Computer sales
Computer Repairs & Virus removal
Wireless Hotspots
CCTV Installation and repair
Network Design and setup
Troubleshooting

```html
<!DOCTYPE html>
<html lang="en">
<head>
<meta charset="utf-8">
<title>KELD Computers – Brand Mark and Business Card</title>
<link rel="stylesheet" href="https://fonts.googleapis.com/css2?family=Roboto+Condensed:wght@400;500;700&display=swap">
<style>
  :root {
    --page: #ffffff;
    --navy: #0d1a8c;
    --royal: #1e37a3;
    --sky: #5b9cf2;
    --paper: #f1f1f1;
    --white: #ffffff;
    --shadow: rgba(0, 0, 0, 0.35);
  }
  * { margin: 0; padding: 0; box-sizing: border-box; }
  html, body {
    width: 1108px;
    height: 1200px;
    overflow: hidden;
    background: var(--page);
    font-family: "Roboto Condensed", "Arial Narrow", sans-serif;
  }
  .canvas { position: relative; width: 1108px; height: 1200px; }

  .brand {
    display: flex;
    align-items: center;
    gap: 14px;
    color: var(--navy);
  }
  .brand-dot { flex: none; border-radius: 50%; background: var(--sky); }
  .brand-name { font-weight: 700; line-height: 1; white-space: nowrap; }
  .brand-tagline { font-weight: 500; color: var(--navy); white-space: nowrap; }

  .mark-standalone { position: absolute; left: 585px; top: 318px; }
  .mark-standalone .brand-dot { width: 96px; height: 96px; }
  .mark-standalone .brand-name { font-size: 62px; }
  .mark-standalone .brand-tagline { font-size: 17px; letter-spacing: 0.6px; margin-top: 8px; }

  .card {
    position: absolute;
    width: 450px;
    height: 272px;
    box-shadow: 2px 3px 5px var(--shadow);
  }
  .card-front {
    left: 150px; top: 520px;
    background: var(--paper);
    z-index: 2;
    display: flex; align-items: center; justify-content: center;
  }
  .card-front .brand { gap: 10px; }
  .card-front .brand-dot { width: 60px; height: 60px; }
  .card-front .brand-name { font-size: 36px; }
  .card-front .brand-tagline { font-size: 11px; margin-top: 4px; }

  .card-back {
    left: 508px; top: 585px;
    background: var(--royal);
    color: var(--white);
    z-index: 1;
    overflow: hidden;
  }
  .back-accent {
    position: absolute; left: 130px; top: 40px;
    width: 220px; height: 180px; border-radius: 50%;
    background: rgba(255, 255, 255, 0.06);
  }
  .contact {
    position: absolute; left: 0; right: 0; top: 66px;
    text-align: center;
  }
  .contact-name { font-size: 19px; font-weight: 400; }
  .contact-name .surname { color: var(--sky); }
  .contact-rule {
    width: 180px; height: 1px; margin: 14px auto 10px;
    background: rgba(255, 255, 255, 0.35);
  }
  .contact-line { font-size: 12px; line-height: 16px; }
  .contact-line .label { color: var(--sky); }
  .contact-web { color: var(--sky); font-weight: 700; font-size: 11px; }
  .services {
    position: absolute; left: 66px; right: 66px; bottom: 26px;
    font-size: 8.2px; font-weight: 500; line-height: 11px;
    text-transform: uppercase; letter-spacing: 0.1px;
  }
</style>
</head>
<body>
<main class="canvas">

  <div class="brand mark-standalone">
    <span class="brand-dot"></span>
    <div>
      <div class="brand-name">KELD Computers</div>
      <div class="brand-tagline">Sundown Technical Services</div>
    </div>
  </div>

  <section class="card card-front">
    <div class="brand">
      <span class="brand-dot"></span>
      <div>
        <div class="brand-name">KELD Computers</div>
        <div class="brand-tagline">Sundown Technical Services</div>
      </div>
    </div>
  </section>

  <section class="card card-back">
    <div class="back-accent"></div>
    <div class="contact">
      <div class="contact-name">Owen <span class="surname">Pelkie</span></div>
      <div class="contact-rule"></div>
      <div class="contact-line"><span class="label">Phone</span> 1300 621 745 <span class="label">Mobile</span> 0457 318 206</div>
      <div class="contact-line">owen@keld.test</div>
      <div class="contact-line contact-web">www.keld.test</div>
    </div>
    <div class="services">
      Computer sales and repairs ~ Virus removal ~ Network design and setup<br>
      CCTV installation and repair ~ Alarm installation ~ Printer sales and setup
    </div>
  </section>

</main>
</body>
</html>
```